Business Card Design Project

Looking for a business card that our customers will remember. We are a high end Travel Agency.
Need a re-memorable classy business card.
Both sides full color.
Must have the following details.
Voyage Harbor Logo (see attached)
4B Kellon Street
Harbourvale Sydney NSW 2190
Phone: 02 9471 3365
Fax: 02 9536 4412
sales@voyageharbor.example
Consultant Name
Anything else you think we need

```html
<!DOCTYPE html>
<html lang="en">
<head>
<meta charset="utf-8">
<title>Voyage Harbor Business Card</title>
<link rel="stylesheet" href="https://fonts.googleapis.com/css2?family=Titillium+Web:wght@300;400;600&display=swap">
<style>
  :root {
    --backdrop: #d9d9d9;
    --card: #ffffff;
    --edge-light: #3fc0d8;
    --edge-dark: #1260b0;
    --edge-rule: #1a5a94;
    --brand: #1f6c99;
    --ink-strong: #222222;
    --ink-soft: #3a3a3a;
  }
  * { margin: 0; padding: 0; box-sizing: border-box; }
  html, body {
    width: 1200px;
    height: 861px;
    overflow: hidden;
    background: var(--backdrop);
  }
  .canvas {
    position: relative;
    width: 1200px;
    height: 861px;
  }
  .business-card {
    position: absolute;
    left: 180px;
    top: 190px;
    width: 840px;
    height: 480px;
    background: var(--card);
    box-shadow: 0 12px 30px rgba(0,0,0,0.18);
    font-family: "Titillium Web", sans-serif;
    overflow: hidden;
  }
  .edge-band {
    position: absolute;
    top: 0;
    bottom: 0;
    width: 52px;
    background: linear-gradient(180deg, var(--edge-light), var(--edge-dark));
  }
  .edge-band::after {
    content: "";
    position: absolute;
    top: 0;
    bottom: 0;
    width: 6px;
    background: var(--edge-rule);
  }
  .edge-band-left { left: 0; }
  .edge-band-left::after { right: -12px; }
  .edge-band-right { right: 0; }
  .edge-band-right::after { left: -12px; }
  .card-content {
    position: absolute;
    inset: 0;
    text-align: center;
  }
  .brand {
    position: absolute;
    top: 60px;
    left: 0;
    right: 0;
    display: flex;
    justify-content: center;
    align-items: center;
    gap: 14px;
  }
  .brand-name {
    font-size: 40px;
    font-weight: 400;
    color: var(--brand);
    letter-spacing: 1px;
  }
  .brand-dot {
    width: 18px;
    height: 18px;
    border-radius: 50%;
    background: var(--brand);
  }
  .consultant-name {
    position: absolute;
    top: 160px;
    left: 0;
    right: 0;
    font-size: 36px;
    font-weight: 600;
    color: var(--ink-strong);
  }
  .contact {
    position: absolute;
    top: 236px;
    left: 0;
    right: 0;
    font-size: 19px;
    font-weight: 300;
    line-height: 26px;
    color: var(--ink-soft);
  }
  .contact-address { margin-bottom: 26px; }
</style>
</head>
<body>
<main class="canvas">
  <section class="business-card">
    <div class="edge-band edge-band-left" aria-hidden="true"></div>
    <div class="edge-band edge-band-right" aria-hidden="true"></div>

    <div class="card-content">
      <div class="brand">
        <span class="brand-name">Voyage Harbor</span>
        <span class="brand-dot"></span>
      </div>
      <h1 class="consultant-name">Consultant Name</h1>
      <div class="contact">
        <p class="contact-address">4B Kellon Street<br>Harbourvale Sydney NSW 2190</p>
        <p class="contact-lines">Phone: 02 9471 3365<br>Fax: 02 9536 4412<br>sales@voyageharbor.example</p>
      </div>
    </div>
  </section>
</main>
</body>
</html>
```